Willow’s Lantern - Childhood Cancer Journey

In 2019, Corbin, my five-year-old, was diagnosed with stage 4 kidney cancer.

From the beginning, I said God would do his part, the doctors will do theirs, and I would do mine to save my son.

Diving into Christian beliefs and research, I learned and applied major shifts in everything we didn’t. Pulling invaluable information from fields like alternative cancer treatments coupled with Tall Reed study, Longevity, Biohacking, Functional Medicine, and microbiome.

Corbin when from stage 4 to cancer-free in 8 months. The journey is and was very difficult, but we’ve learned and been able to help countless others.

Industry/Entity Type

Health, Wellness, Mindset, Adversity

Requirements
Nice to have
• Bright with feelings of warmth

```html
<!DOCTYPE html>
<html lang="en">
<head>
<meta charset="utf-8">
<title>Willow’s Lantern — Book Cover</title>
<link rel="stylesheet" href="https://fonts.googleapis.com/css2?family=PT+Serif:wght@400&family=Poppins:wght@400&display=swap">
<style>
  :root {
    --page-bg: #ecebe8;
    --cover-bg: #ffffff;
    --title-red: #e2353f;
    --title-purple: #4b3c8e;
    --subtitle-navy: #3a2f86;
    --rule-red: #d8343c;
    --art-warm: #f9dcb6;
    --art-soft: #f6c9b8;
  }
  * { margin: 0; padding: 0; box-sizing: border-box; }
  html, body {
    width: 1200px;
    height: 1200px;
    overflow: hidden;
    background: var(--page-bg);
  }
  .canvas {
    width: 1200px;
    height: 1200px;
    display: flex;
    align-items: center;
    justify-content: center;
  }
  .book-cover {
    width: 760px;
    height: 1140px;
    background: var(--cover-bg);
    box-shadow: 0 10px 30px rgba(0,0,0,0.12);
    display: flex;
    flex-direction: column;
    align-items: center;
    padding-top: 58px;
  }
  .title {
    font-family: "PT Serif", Georgia, serif;
    font-weight: 400;
    text-align: center;
    line-height: 0.92;
  }
  .title-top {
    display: block;
    color: var(--title-red);
    font-size: 146px;
    letter-spacing: 1px;
  }
  .title-bottom {
    display: block;
    color: var(--title-purple);
    font-size: 128px;
    letter-spacing: 6px;
    margin-top: 6px;
  }
  .cover-art {
    margin-top: 40px;
    width: 440px;
    height: 400px;
    background: linear-gradient(180deg, var(--art-warm) 0%, var(--art-soft) 100%);
  }
  .subtitle-block {
    margin-top: 26px;
    width: 600px;
    border-top: 1.5px solid var(--rule-red);
    border-bottom: 1.5px solid var(--rule-red);
    padding: 14px 0 16px;
  }
  .subtitle {
    font-family: "Poppins", Arial, sans-serif;
    font-size: 23px;
    line-height: 1.12;
    color: var(--subtitle-navy);
    text-align: center;
    white-space: nowrap;
  }
  .author {
    margin-top: 30px;
    font-family: "PT Serif", Georgia, serif;
    font-size: 62px;
    letter-spacing: 7px;
    color: var(--title-red);
    text-transform: uppercase;
  }
</style>
</head>
<body>
<main class="canvas">
  <article class="book-cover">
    <h1 class="title">
      <span class="title-top">Willow’s</span>
      <span class="title-bottom">LANTERN</span>
    </h1>

    <div class="cover-art" role="img" aria-label="Illustration of a smiling father holding his young son, who holds an ice pop, before a warm peach backdrop"></div>

    <div class="subtitle-block">
      <p class="subtitle">A Loving Father, Determined to Guide<br>His Cancer-Stricken Son’s Journey to a Cure,<br>Discovers the Tall Reed Protocol of Nourishing<br>the Body to Optimum Health</p>
    </div>

    <p class="author">Marcus Ellery</p>
  </article>
</main>
</body>
</html>
```